brownie sticker

i need a sticker to wrap around a clear rectangle box that will contain chocolate brownies. the sticker must be 17cm x 7 cm.
the sticker will be placed in the folowing direction.
7cm of the sticker on front of box, 3cm for each side of the box, and 4 cm on the bottom to seal the box closed.
I HAVE ATTACHED A VERY ROUGH PICTURE FOR YOU TO SEE POSITION AND DIRECTION OF STICKER.

Target Market(s)

our product will be mainly seen in upmarket grocery stores and farmers markets.

Requirements
Must have
• IT MUST CONTAIN THE FOLLOWING IN SMALL PRINT at the bottom of the sticker...
produced by marigolds bakehouse
48 kellow st
cheltenham
vic 3274
ph: 047658913
email: marigoldsbakehouse@mailbrook.net

```html
<!DOCTYPE html>
<html lang="en">
<head>
<meta charset="utf-8">
<title>Marigold's Bakehouse – Brownie Box Sticker</title>
<link rel="stylesheet" href="https://fonts.googleapis.com/css2?family=Open+Sans:wght@600&display=swap">
<style>
  :root {
    --page: #ffffff;
    --chocolate: #5c2e12;
    --chocolate-dark: #2e1208;
    --cream: #fbf1b0;
    --gold-light: #f6c452;
    --gold: #d9992a;
    --gold-deep: #a8611a;
    --ink: #4a2414;
  }
  html, body {
    margin: 0;
    padding: 0;
    overflow: hidden;
    background: var(--page);
  }
  .canvas {
    position: relative;
    width: 1000px;
    height: 1200px;
    overflow: hidden;
    background: var(--page);
  }
  .sticker-pattern {
    position: absolute;
    left: 281px;
    top: 83px;
    width: 416px;
    height: 1011px;
    background: var(--chocolate);
  }
  .sticker-art {
    position: absolute;
    inset: 0;
  }
  .brand-name {
    position: absolute;
    left: 340px;
    top: 578px;
    width: 320px;
    margin: 0;
    text-align: center;
    color: var(--ink);
    font-family: "Open Sans", sans-serif;
    font-weight: 600;
    font-size: 26px;
    line-height: 1;
  }
  .small-print {
    position: absolute;
    left: 297px;
    top: 1043px;
    margin: 0;
    font-family: "Open Sans", sans-serif;
    font-weight: 600;
    font-size: 7px;
    line-height: 10.5px;
    color: var(--chocolate-dark);
  }
</style>
</head>
<body>
<main class="canvas">
  <div class="sticker-pattern" role="img" aria-label="Swirling dark chocolate flourish pattern across the sticker"></div>

  <svg class="sticker-art" width="1000" height="1200" viewBox="0 0 1000 1200" aria-hidden="true">
    <defs>
      <linearGradient id="gold-ring" x1="0" y1="0" x2="1" y2="1">
        <stop offset="0" stop-color="#f6c452"/>
        <stop offset="0.45" stop-color="#a8611a"/>
        <stop offset="0.75" stop-color="#f6c452"/>
        <stop offset="1" stop-color="#d9992a"/>
      </linearGradient>
      <linearGradient id="gold-band" x1="0" y1="0" x2="0" y2="1">
        <stop offset="0" stop-color="#f6c452"/>
        <stop offset="0.4" stop-color="#a8611a"/>
        <stop offset="1" stop-color="#d9992a"/>
      </linearGradient>
    </defs>

    <circle class="seal-ring" cx="489" cy="585" r="243" fill="url(#gold-ring)"/>
    <circle class="seal-inner-edge" cx="489" cy="585" r="222" fill="#d9992a"/>
    <circle class="seal-shadow" cx="497" cy="583" r="212" fill="#2e1208"/>
    <circle class="seal-face" cx="500" cy="582" r="200" fill="#fbf1b0"/>
    <path class="seal-swoosh" d="M330 470 Q 420 380 600 465" fill="none" stroke="#d9992a" stroke-width="5" stroke-linecap="round" opacity="0.8"/>

    <path class="base-band" d="M281 1030 Q 489 900 697 1030 L697 1094 L281 1094 Z" fill="url(#gold-band)"/>
    <path class="base-band-edge" d="M281 1030 Q 489 900 697 1030" fill="none" stroke="#f6c452" stroke-width="4"/>
  </svg>

  <p class="brand-name">Marigold’s Bakehouse</p>

  <p class="small-print">
    Produced by Marigold’s Bakehouse<br>
    48 Kellow St, Cheltenham, VIC 3274<br>
    Tel: 047658913<br>
    Email: marigoldsbakehouse@mailbrook.net
  </p>
</main>
</body>
</html>
```